Company rebrand announcement

We're renaming and rebranding. our company - I need an email design that we can send out as an update to our customers and suppliers. I can provide the text but would like the design to allow me to write the text myself as we would like to personalise it and mail merge. But will be something like this:

The past year has been incredible for k7webworks and Quiet Harbor. If you've been following our story you'll know we've been working hard at being a couple over the last year and now we're ready to make it official!

As part of the official merge we'll be renaming to wefoundpath - a name that highlights our passion for connecting people and technology helping make our everyday lives that little bit easier.

With a new name comes a few changes, new website, new logo, new clothes - the excitement is real! THE MOST exciting parts though are that we have the same great team and will continue to provide the same great service with the agility and trust you have come to love and expect from us.

We'll send out the details over the coming weeks to make sure we all stay connected and if you have any questions in the meantime or anything you need us to do, please reach out to any one of us and we'll get right back to you.

Thanks,
Doreen, Glen and Wade

```html
<!DOCTYPE html>
<html lang="en">
<head>
<meta charset="utf-8">
<title>We Found Path – Rebrand Announcement</title>
<link href="https://fonts.googleapis.com/css2?family=Roboto:wght@400;500;700&display=swap" rel="stylesheet">
<style>
  :root {
    --ink: #1f1f1f;
    --yellow: #f2bb0a;
    --yellow-deep: #e9b20a;
    --yellow-pale: #fbe08a;
    --muted: #9a9a9a;
    --footer: #050505;
    --white: #ffffff;
  }
  * { margin: 0; padding: 0; box-sizing: border-box; }
  html, body { width: 1200px; height: 3024px; overflow: hidden; background: var(--white); }
  body { font-family: "Roboto", Arial, sans-serif; color: var(--ink); position: relative; }

  .line { display: block; white-space: nowrap; }
  .justified .line { text-align: justify; text-align-last: justify; }
  .justified .line.last { text-align-last: left; }

  .hero { position: absolute; left: 0; top: 0; width: 1200px; height: 786px; overflow: hidden; }
  .hero-art { position: absolute; left: 0; top: 0; }
  .brand { position: absolute; left: 90px; top: 232px; }
  .brand-row { display: flex; align-items: center; gap: 16px; }
  .brand-dot { width: 30px; height: 30px; border-radius: 50%; background: var(--yellow); }
  .brand-name { font-size: 54px; font-weight: 700; color: var(--ink); letter-spacing: -0.5px; line-height: 1; }
  .brand-tagline { margin-top: 16px; font-size: 19px; font-weight: 700; color: var(--ink); letter-spacing: -0.2px; }
  .hero-lead { position: absolute; left: 95px; top: 492px; font-size: 36px; font-weight: 500; line-height: 57px; }

  .story-band {
    position: absolute; left: 0; top: 786px; width: 1200px; height: 333px;
    background: linear-gradient(100deg, var(--yellow-deep), var(--yellow) 50%, var(--yellow-deep));
    display: flex; align-items: center; justify-content: center;
  }
  .story-band p { text-align: center; color: var(--white); font-size: 37px; font-weight: 700; line-height: 62px; }

  .merge-photo {
    position: absolute; left: 86px; top: 1197px; width: 453px; height: 366px;
    border: 4px solid #cfcfcf;
    background: linear-gradient(135deg, #d9dee3 0%, #6b6f78 35%, #8a5fd0 60%, #c8d3da 100%);
  }
  .merge-copy {
    position: absolute; left: 623px; top: 1211px; width: 483px;
    font-size: 26px; font-weight: 500; line-height: 55.5px;
  }

  .city-band {
    position: absolute; left: 0; top: 1659px; width: 1200px; height: 584px;
    background: linear-gradient(180deg, #c9b99a 0%, #8a7d78 35%, #6a5560 60%, #c98a3c 85%, #5a4660 100%);
  }
  .city-panel {
    position: absolute; left: 112px; top: 108px; width: 976px; height: 360px;
    background: rgba(60, 50, 60, 0.55);
    padding: 36px 58px 0;
  }
  .city-panel p { color: var(--white); font-size: 26px; font-weight: 700; line-height: 55.5px; }
  .city-panel .line.last { text-align: center; text-align-last: center; }

  .closing-copy {
    position: absolute; left: 90px; top: 2372px; width: 483px;
    font-size: 26px; font-weight: 500; line-height: 55.5px;
  }
  .sign-off { position: absolute; left: 90px; top: 2766px; font-size: 26px; font-weight: 500; line-height: 48px; }
  .sign-off .thanks { color: var(--muted); }
  .team-photo { position: absolute; left: 623px; top: 2327px; }

  .footer {
    position: absolute; left: 0; top: 2914px; width: 1200px; height: 110px;
    background: var(--footer); color: var(--white);
    display: flex; align-items: center; justify-content: center;
    font-size: 20px;
  }
</style>
</head>
<body>

<header class="hero">
  <svg class="hero-art" width="1200" height="786" viewBox="0 0 1200 786">
    <defs>
      <linearGradient id="heroPhoto" x1="0" y1="0" x2="1" y2="1">
        <stop offset="0" stop-color="#f4f1ee"/>
        <stop offset="0.5" stop-color="#d9cfc8"/>
        <stop offset="1" stop-color="#c79a8e"/>
      </linearGradient>
    </defs>
    <circle cx="1010" cy="160" r="545" fill="var(--yellow)"/>
    <circle cx="1030" cy="150" r="530" fill="var(--yellow-pale)"/>
    <circle cx="1045" cy="140" r="520" fill="url(#heroPhoto)" role="img" aria-label="Woman relaxing in an armchair looking at her phone"/>
  </svg>

  <div class="brand">
    <div class="brand-row">
      <span class="brand-dot"></span>
      <span class="brand-name">We Found Path</span>
    </div>
    <div class="brand-tagline">CONNECTING PEOPLE EVERY DAY</div>
  </div>

  <p class="hero-lead">
    <span class="line">The past year has been</span>
    <span class="line">incredible for k7webworks</span>
    <span class="line">and Quiet Harbor.</span>
  </p>
</header>

<section class="story-band">
  <p>
    <span class="line">If you've been following our story you'll know we've</span>
    <span class="line">been working hard at being a couple over the last year</span>
    <span class="line">and now we're ready to make it official!</span>
  </p>
</section>

<div class="merge-photo" role="img" aria-label="Hand holding a phone to a contactless payment terminal"></div>
<p class="merge-copy justified">
  <span class="line">As part of the official merge we'll be</span>
  <span class="line">renaming it to wefoundpath - a name</span>
  <span class="line">that highlights our passion for</span>
  <span class="line">connecting people and technology</span>
  <span class="line">helping make our everyday lives that</span>
  <span class="line last">little bit easier.</span>
</p>

<section class="city-band" role="img" aria-label="City skyline at dusk with glowing network lines">
  <div class="city-panel">
    <p class="justified">
      <span class="line">With a new name comes a few changes, new website, new logo, new</span>
      <span class="line">clothes - the excitement is real! THE MOST exciting parts though</span>
      <span class="line">are that we have the same great team and will continue to provide</span>
      <span class="line">the same great service with the agility and trust you have come to</span>
      <span class="line last">love and expect from us.</span>
    </p>
  </div>
</section>

<p class="closing-copy justified">
  <span class="line">We'll send out the details over the</span>
  <span class="line">coming weeks to make sure we all</span>
  <span class="line">stay connected and if you have any</span>
  <span class="line">questions in the meantime or</span>
  <span class="line">anything you need us to do, please</span>
  <span class="line">reach out to any one of us and we'll</span>
  <span class="line last">get right back to you.</span>
</p>
<div class="sign-off">
  <div class="thanks">Thanks,</div>
  <div>Doreen, Glen and Wade</div>
</div>

<svg class="team-photo" width="484" height="500" viewBox="0 0 484 500">
  <defs>
    <linearGradient id="teamPhoto" x1="0" y1="0" x2="1" y2="1">
      <stop offset="0" stop-color="#8d8a86"/>
      <stop offset="0.5" stop-color="#e7e2da"/>
      <stop offset="1" stop-color="#c9b88c"/>
    </linearGradient>
  </defs>
  <circle cx="242" cy="248" r="240" fill="none" stroke="var(--yellow)" stroke-width="5"/>
  <circle cx="242" cy="248" r="226" fill="url(#teamPhoto)" role="img" aria-label="Two colleagues smiling while looking at a tablet"/>
</svg>

<footer class="footer">© 2024 we found path &nbsp;| All rights reserved.</footer>

</body>
</html>
```